Adelaide based cleaning and remediation business needs a website design

We are launching a new company with no clients as yet so we don't have the benefit of Veltrano Ratings to build confidence. We can use our  past work history with other employers in the industry to give some credibility. Happy to use any colour scheme as long as it look interesting when people click on the site it gets there attention. enquiry . I have supplied a mock up the important information and various photos as they tell a lot of the story.

```html
<!DOCTYPE html>
<html lang="en">
<head>
<meta charset="utf-8">
<title>Karrawin Services Pty Ltd</title>
<link href="https://fonts.googleapis.com/css2?family=Black+Ops+One&family=Poppins:ital,wght@0,400;0,500;0,600;0,700;1,400&display=swap" rel="stylesheet">
<style>
:root{
  --orange:#f39c12;
  --purple:#b064a0;
  --purple-deep:#a14f94;
  --ink:#1f1f1f;
  --text:#3a3a3a;
  --dark:#2a2a2a;
  --white:#ffffff;
  --card:#f6eef5;
}
*{margin:0;padding:0;box-sizing:border-box}
html,body{width:1200px;height:3856px;overflow:hidden}
body{
  position:relative;font-family:"Poppins",sans-serif;color:var(--text);
  background:
    radial-gradient(ellipse 520px 420px at 120px 420px,#fde3e6 0%,rgba(253,227,230,0) 100%),
    radial-gradient(ellipse 500px 420px at 1180px 1350px,#fff0dc 0%,rgba(255,240,220,0) 100%),
    radial-gradient(ellipse 480px 420px at 0 2150px,#f6e6f3 0%,rgba(246,230,243,0) 100%),
    radial-gradient(ellipse 560px 420px at 1100px 2950px,#fde4e4 0%,rgba(253,228,228,0) 100%),
    #ffffff;
}
.abs{position:absolute}
.display{font-family:"Black Ops One",sans-serif;color:var(--ink);letter-spacing:1px}
.center{left:0;width:1200px;text-align:center}

/* nav */
.brand{left:88px;top:38px;font-family:"Poppins",sans-serif;font-weight:700;font-size:18px;color:var(--ink);display:flex;align-items:center;gap:8px}
.brand-dot{width:14px;height:14px;background:var(--ink)}
.nav a{position:absolute;top:40px;font-size:14px;color:var(--ink);text-decoration:none}
.nav .active{font-weight:600}
.btn{position:absolute;display:flex;align-items:center;justify-content:center;border-radius:30px;font-weight:700;font-size:12px;text-transform:uppercase;text-decoration:none}
.btn-orange{background:var(--orange);color:var(--white)}
.btn-outline{border:1.5px solid var(--ink);color:var(--ink);background:var(--white)}
.btn-white{background:var(--white);color:var(--ink)}

/* hero */
.hero-title{left:88px;top:240px;font-size:64px;line-height:64px}
.photo{position:absolute;border-radius:50%}

/* about */
.about-title{top:776px;font-size:46px;color:var(--white)}
.about p{position:absolute;left:170px;width:860px;text-align:center;color:var(--white);font-size:14.5px;line-height:22px}

/* services */
.section-title{font-size:44px}
.svc-card{left:409px;top:1325px;width:382px;height:452px;background:linear-gradient(180deg,#ffffff,var(--card));border-radius:14px}
.svc-name{font-family:"Black Ops One",sans-serif;font-size:21px;line-height:25px;color:var(--ink);text-align:center;width:300px}
.svc-text{left:432px;top:1620px;width:336px;text-align:center;font-size:14px;line-height:22px}
.note{top:1820px;left:250px;width:700px;text-align:center;font-size:14px;line-height:23px}
.rule{left:88px;top:1925px;width:1024px;height:1px;background:#d9d2d7}

/* pricing */
.pricing-title{left:644px;top:2118px;font-size:42px}
.pricing-text{left:644px;top:2184px;width:380px;font-size:14.5px;line-height:22.2px}

/* reviews */
.review-sub{top:2580px;font-size:16px}
.review-box{left:210px;top:2631px;width:780px;height:344px;background:var(--orange);border-radius:42px}
.quote-mark{left:0;top:2676px;width:1200px;text-align:center;font-family:"Black Ops One",sans-serif;font-size:120px;line-height:120px;color:var(--white)}
.review-text{left:250px;width:700px;text-align:center;color:var(--white);font-style:italic;font-size:18.5px;line-height:24px}
.reviewer{top:2896px;font-family:"Black Ops One",sans-serif;font-size:20px;color:var(--white)}
.pager{top:2740px;width:58px;height:127px;background:var(--white);border:1px solid #e4e4e4;border-radius:12px;display:flex;align-items:center;justify-content:center;font-family:"Black Ops One",sans-serif;font-size:12px;color:var(--ink)}

/* quote */
.quote-sub{top:3138px;font-size:17.5px;color:#555}
.phone-icon{left:494px;top:3189px;width:52px;height:52px;border-radius:50%;background:var(--orange);display:flex;align-items:center;justify-content:center}
.phone-number{left:558px;top:3196px;font-size:26px;font-weight:600;color:var(--ink);letter-spacing:.5px}

/* footer */
.footer-brand{left:110px;top:3595px;font-size:26px;font-weight:700;color:var(--white);width:230px;text-align:center}
.footer-title{font-family:"Black Ops One",sans-serif;font-size:20px;color:var(--white);letter-spacing:1px}
.footer-item{color:var(--white);font-size:11.5px;line-height:18px}
.f-icon{position:absolute;left:-20px;top:2px}
.social{top:3554px;width:38px;height:38px;border-radius:50%;background:#3a3a3a;color:var(--white);font-size:10px;font-weight:600;display:flex;align-items:center;justify-content:center}
.footer-rule{left:88px;top:3806px;width:1024px;height:1px;background:#4a4a4a}
.copyright{top:3825px;font-size:13px;color:var(--white)}
.pay{top:3822px;width:33px;height:23px;border-radius:3px;background:var(--white);color:var(--ink);font-size:8px;font-weight:600;display:flex;align-items:center;justify-content:center}
</style>
</head>
<body>

<!-- header -->
<div class="abs brand"><span class="brand-dot"></span>Karrawin</div>
<nav class="nav">
  <a class="active" style="left:548px">HOME</a>
  <a style="left:642px">About Us</a>
  <a style="left:757px">Services</a>
  <a style="left:869px">Pricing</a>
</nav>
<a class="btn btn-orange" style="left:962px;top:27px;width:148px;height:46px">Read More</a>

<!-- hero -->
<div class="abs" role="img" aria-label="Orange decorative burst" style="left:515px;top:128px;width:150px;height:160px;border-radius:50%;background:radial-gradient(circle,rgba(243,156,18,.55) 0%,rgba(243,156,18,0) 70%)"></div>
<h1 class="abs display hero-title">KARRAWIN<br>SERVICES<br>PTY LTD</h1>
<a class="btn btn-orange" style="left:88px;top:463px;width:195px;height:45px;font-size:11px">Dirty Job Cleaners</a>
<a class="btn btn-outline" style="left:289px;top:463px;width:146px;height:45px;font-size:11px">Get a Quote</a>

<svg class="abs" style="left:0;top:600px" width="1200" height="680" viewBox="0 0 1200 680" aria-hidden="true">
  <path d="M0 215 C260 90 620 20 1200 18 L1200 665 C1060 540 700 495 0 530 Z" fill="var(--purple)"/>
</svg>

<div class="photo" role="img" aria-label="Cleaner in protective suit and respirator clearing fire-damaged debris" style="left:534px;top:115px;width:600px;height:600px;background:radial-gradient(circle at 60% 45%,#3d8fd1 0%,#2f5f8c 30%,#3b3530 65%,#1d1b19 100%)"></div>

<!-- about -->
<section class="about">
  <h2 class="abs display center about-title">ABOUT US</h2>
  <p style="top:845px">Adelaide-based Karrawin Services is a family-run organisation. We have been in operation for more than two decades. We've gained some knowledge about cleaning and squalor removal services throughout the years.</p>
  <p style="top:904px">As a small South Australian company, we base everything on responsibility honesty and fairness .We are aware of the confidence you put in us when you seek our help.</p>
  <a class="btn btn-white" style="left:529px;top:973px;width:141px;height:42px">Read More</a>
</section>

<!-- services -->
<h2 class="abs display center section-title" style="top:1232px">OUR SERVICES</h2>

<div class="photo" role="img" aria-label="Pigeon perched on a window ledge" style="left:143px;top:1385px;width:202px;height:202px;background:radial-gradient(circle at 50% 55%,#8b8f94 0%,#c7cbcf 55%,#e6e8ea 100%)"></div>
<div class="abs svc-name" style="left:94px;top:1617px">PIGEON<br>WASTE</div>

<div class="abs svc-card"></div>
<div class="photo" role="img" aria-label="Worker pressure cleaning a burnt surface" style="left:499px;top:1324px;width:202px;height:202px;background:radial-gradient(circle at 50% 60%,#2a2a2a 0%,#5a5550 50%,#a59a8a 100%)"></div>
<div class="abs svc-name" style="left:450px;top:1554px">FIRE DAMAGE<br>CLEAN OUTS</div>
<p class="abs svc-text">Removal of debris; On site cleaning of contents; Cleaning of carpets and upholstered items; Catalogue all contents for packing and storage Pressure cleaning of contaminated surfaces;</p>

<div class="photo" role="img" aria-label="Cleaner in protective suit sorting debris in a roof space" style="left:854px;top:1385px;width:202px;height:202px;background:radial-gradient(circle at 50% 55%,#d9d6d2 0%,#6e665c 55%,#2b2824 100%)"></div>
<div class="abs svc-name" style="left:805px;top:1617px">SQULAOR ESTATE<br>CLEAN UPS</div>

<p class="abs note">We are fully insured for 20 million public liability and our team have current police and working with vulnerable people clearances</p>
<div class="abs rule"></div>

<!-- pricing -->
<div class="photo" role="img" aria-label="Cluttered shed with shelves full of stored items" style="left:163px;top:2006px;width:422px;height:422px;background:radial-gradient(circle at 45% 50%,#9a7a55 0%,#6d5238 45%,#3c2f25 100%)"></div>
<h2 class="abs display pricing-title">PRICING</h2>
<p class="abs pricing-text">Prices provided in terms of the number of hours and service required or as a fixed quotation according to the quantity of clutter, pigeon faeces, and mould disposal expenses; however, hoarding cleaning can be different as this may require sorting and can require more organisation.</p>

<!-- reviews -->
<h2 class="abs display center section-title" style="top:2516px">REVIEWS</h2>
<p class="abs display center review-sub">ONLY THE BEST SERVICE FOR OUR CUSTOMERS</p>

<div class="abs pager" style="left:128px">PREV</div>
<div class="abs pager" style="left:1013px">NEXT</div>
<div class="abs review-box"></div>
<div class="abs quote-mark">&ldquo;</div>
<p class="abs review-text" style="top:2761px">Declan and his team arrived the next morning to clean up a rental property my husband and I own which and had been trashed &nbsp;by the tenants.</p>
<p class="abs review-text" style="top:2824px">He was the only contractor to return my call. They did an amazing job and also deodorised the house for no extra charge.</p>
<p class="abs center reviewer">MARNIE DELACOURT, SATISFIED CUSTOMER</p>

<!-- quick quote -->
<h2 class="abs display center" style="top:3064px;font-size:46px">GET A QUICK QUOTE</h2>
<p class="abs center quote-sub">Send a text to Karrawin Services Please enter your mobile number or email and message</p>
<div class="abs phone-icon">
  <svg width="26" height="26" viewBox="0 0 24 24" fill="none" stroke="#fff" stroke-width="2"><circle cx="12" cy="12" r="9"/><path d="M9 8.5c0 4 2.5 6.5 6.5 6.5l1-1.8-2-1-1 .8c-1.2-.5-2-1.3-2.5-2.5l.8-1-1-2z" fill="#fff" stroke="none"/></svg>
</div>
<div class="abs phone-number">0412555018</div>

<!-- footer -->
<svg class="abs" style="left:0;top:3290px" width="1200" height="566" viewBox="0 0 1200 566" aria-hidden="true">
  <path d="M0 290 C300 -20 800 -20 1200 50 L1200 566 L0 566 Z" fill="var(--purple-deep)"/>
  <path d="M0 370 C300 20 800 20 1200 90 L1200 566 L0 566 Z" fill="var(--dark)"/>
</svg>

<div class="abs footer-brand">Karrawin<br>Services</div>

<h3 class="abs footer-title" style="left:434px;top:3508px">CONTACT US</h3>
<div class="abs footer-item" style="left:454px;top:3553px">
  <svg class="f-icon" width="11" height="13" viewBox="0 0 12 14"><path d="M6 0a5 5 0 0 0-5 5c0 3.5 5 9 5 9s5-5.5 5-9a5 5 0 0 0-5-5zm0 7a2 2 0 1 1 0-4 2 2 0 0 1 0 4z" fill="var(--orange)"/></svg>
  Location:<br>12B Coralie Street Netherby<br>SA 5062
</div>
<div class="abs footer-item" style="left:454px;top:3618px">
  <svg class="f-icon" width="12" height="12" viewBox="0 0 24 24"><path d="M6.6 10.8a15 15 0 0 0 6.6 6.6l2.2-2.2c.3-.3.7-.4 1-.2 1.1.4 2.3.6 3.6.6.6 0 1 .4 1 1V20c0 .6-.4 1-1 1A17 17 0 0 1 3 4c0-.6.4-1 1-1h3.5c.6 0 1 .4 1 1 0 1.3.2 2.5.6 3.6.1.3 0 .7-.2 1z" fill="var(--orange)"/></svg>
  Call Us:<br>Declan or Anand 0412 555 018
</div>
<div class="abs footer-item" style="left:454px;top:3671px">
  <svg class="f-icon" width="12" height="10" viewBox="0 0 24 18"><rect width="24" height="18" rx="2" fill="var(--orange)"/><path d="M1 2l11 8 11-8" stroke="#2a2a2a" stroke-width="2" fill="none"/></svg>
  Email Us:<br>admin@karrawinservices.com
</div>
<p class="abs footer-item" style="left:434px;top:3722px;width:440px">&nbsp;&nbsp;Got more questions about our clean-up services and what we offer?<br>Get in touch today M 0412 555 018</p>

<h3 class="abs footer-title" style="left:706px;top:3508px">BUSINESS HOURS</h3>
<div class="abs footer-item" style="left:728px;top:3553px">
  <svg class="f-icon" width="12" height="12" viewBox="0 0 24 24"><circle cx="12" cy="12" r="11" fill="var(--orange)"/><path d="M12 6v6l4 2" stroke="#2a2a2a" stroke-width="2" fill="none"/></svg>
  Monday to Saturday<br>8:00 am to 4:00 pm
</div>

<div class="abs social" style="left:1005px">Nook</div>
<div class="abs social" style="left:1051px">Pixa</div>

<div class="abs footer-rule"></div>
<p class="abs center copyright">Copyrights 2025,All Rights Reserved</p>
<div class="abs pay" style="left:860px">Tapro</div>
<div class="abs pay" style="left:903px">Qpay</div>
<div class="abs pay" style="left:946px">Zenn</div>
<div class="abs pay" style="left:989px">Corvex</div>
<div class="abs pay" style="left:1032px">Mirel</div>
<div class="abs pay" style="left:1075px">Ostra</div>

</body>
</html>
```